Visitenkarten-Design für Forschungs- und Beratungsunternehmen
Zielgruppe
*Veridora' ist ein Forschungs- und Beratungsunternehmen für Lebensmittelwirkungen. Unsere Angebote sind: Vorträge, Workshops, Seminare und Coaching. Die Zielgruppen sind Pädagogen, Mediziner, Psychologen u.a.m.
Aufgabenstellung
Bei Bedarf kann die Gestaltung der Visitenkarte auch auf die Rückseite ausgedehnt werden.

```html
<!DOCTYPE html>
<html lang="de">
<head>
<meta charset="utf-8">
<title>Veridora – Visitenkarte</title>
<link rel="stylesheet" href="https://fonts.googleapis.com/css2?family=Poppins:wght@300;400;600;700&display=swap">
<style>
  :root {
    --backdrop: #c9cdd1;
    --card-navy: #1e2c40;
    --card-navy-deep: #1a2639;
    --text-light: #eef1f5;
    --text-soft: #c9d0da;
    --accent-dot: #2f8fd6;
  }
  * { margin: 0; padding: 0; box-sizing: border-box; }
  html, body {
    width: 1200px;
    height: 900px;
    overflow: hidden;
    background: var(--backdrop);
    font-family: "Poppins", sans-serif;
  }
  .canvas {
    width: 1200px;
    height: 900px;
    display: flex;
    flex-direction: column;
    align-items: center;
    justify-content: center;
    gap: 44px;
  }
  .card {
    position: relative;
    width: 600px;
    height: 388px;
    background: linear-gradient(135deg, var(--card-navy-deep), var(--card-navy));
    color: var(--text-light);
    box-shadow: 0 6px 18px rgba(0, 0, 0, 0.18);
  }
  .brand {
    display: flex;
    align-items: center;
    gap: 10px;
    font-weight: 300;
    letter-spacing: 0.06em;
    color: var(--text-light);
  }
  .brand-dot {
    width: 10px;
    height: 10px;
    border-radius: 50%;
    background: var(--accent-dot);
  }
  .card-front .brand {
    position: absolute;
    right: 70px;
    bottom: 100px;
    font-size: 30px;
  }
  .card-back .brand {
    position: absolute;
    left: 44px;
    top: 40px;
    font-size: 22px;
  }
  .person {
    position: absolute;
    left: 370px;
    top: 40px;
  }
  .person-name {
    font-weight: 700;
    font-size: 17px;
    letter-spacing: 0.02em;
  }
  .person-role {
    font-weight: 300;
    font-size: 13px;
    color: var(--text-soft);
    letter-spacing: 0.03em;
  }
  .contact {
    position: absolute;
    left: 350px;
    top: 190px;
    display: grid;
    grid-template-columns: 28px auto;
    row-gap: 4px;
    font-size: 14px;
    font-weight: 300;
    letter-spacing: 0.03em;
  }
  .contact dt { color: var(--text-soft); }
  .contact dd { color: var(--text-light); }
  .hours {
    position: absolute;
    left: 60px;
    bottom: 44px;
    font-size: 14px;
    font-weight: 300;
    letter-spacing: 0.03em;
  }
  .hours strong { font-weight: 600; }
</style>
</head>
<body>
<main class="canvas">
  <section class="card card-front" aria-label="Vorderseite">
    <div class="brand"><span class="brand-dot"></span><span>Veridora</span></div>
  </section>

  <section class="card card-back" aria-label="Rückseite">
    <div class="brand"><span class="brand-dot"></span><span>Veridora</span></div>
    <div class="person">
      <p class="person-name">Lukas Brenner</p>
      <p class="person-role">Geschäftsführer</p>
    </div>
    <dl class="contact">
      <dt>A:</dt><dd>Lindenweg 18</dd>
      <dt></dt><dd>CH-4302 Talberg</dd>
      <dt>T:</dt><dd>+41 61 555 24 80</dd>
      <dt>E:</dt><dd>info@veridora.ch</dd>
      <dt>W:</dt><dd>www.veridora.ch</dd>
    </dl>
    <p class="hours"><strong>MO – FR</strong> 10.00 h – 19.00 h</p>
  </section>
</main>
</body>
</html>
```